"contact us" Flyer for Marketing Drop-offs

We need a simple 3rd of a page (3 3/4" x 8 1/2") flyer made for quick customer interaction.

These should display our logo, tagline, and our contact information. The background should incorporate the attached picture/color scheme.

This flyer will be offering an incentive to be determined at a later date.

Industry/Entity Type

Legal

Font styles to use
Serif
Sans Serif

Colors
0255a3
33a6d7
876aae

Requirements
Must have
• proper color scheme, simple/modern layout, attached logo
Nice to have
• creativity with working, placement
Should not have
• extra/meaningless characters, shapes

```html
<!DOCTYPE html>
<html lang="en">
<head>
<meta charset="utf-8">
<title>Plains Ledger – Contact Flyer</title>
<link rel="stylesheet" href="https://fonts.googleapis.com/css2?family=Oswald:wght@600;700&family=Raleway:wght@400;500;600;700&display=swap">
<style>
  :root {
    --navy: #1c3b93;
    --royal: #0255a3;
    --sky: #33a6d7;
    --violet: #876aae;
    --paper: #ffffff;
    --input-text: #9a9ca3;
  }
  * { box-sizing: border-box; margin: 0; padding: 0; }
  html, body { width: 1200px; height: 3041px; overflow: hidden; background: var(--paper); }
  .flyer {
    position: relative;
    width: 1200px;
    height: 3041px;
    overflow: hidden;
    background: var(--paper);
    font-family: "Raleway", sans-serif;
  }
  .backdrop { position: absolute; left: 0; top: 0; width: 1200px; height: 2000px; }
  .brand-header {
    position: absolute;
    top: 150px;
    right: 70px;
    font-family: "Oswald", sans-serif;
    font-weight: 700;
    font-size: 118px;
    line-height: 1;
    color: var(--navy);
    letter-spacing: -1px;
  }
  .tagline {
    position: absolute;
    left: 171px;
    top: 734px;
    width: 980px;
    color: #fff;
    font-size: 46px;
    line-height: 56px;
    font-weight: 400;
  }
  .tagline strong { font-weight: 700; }
  .accent-bars { position: absolute; left: 66px; top: 734px; }
  .accent-bars span { position: absolute; top: 0; width: 18px; height: 222px; }
  .accent-bars .bar-dark { left: 0; background: var(--royal); }
  .accent-bars .bar-light { left: 26px; top: 22px; height: 200px; background: var(--sky); }
  .search {
    position: absolute;
    left: 108px;
    top: 1147px;
    width: 981px;
    height: 80px;
    display: flex;
  }
  .search-field {
    flex: 1;
    background: #fff;
    color: var(--input-text);
    font-size: 28px;
    display: flex;
    align-items: center;
    padding-left: 36px;
  }
  .search-button {
    width: 252px;
    background: var(--sky);
    color: #fff;
    font-size: 30px;
    display: flex;
    align-items: center;
    justify-content: center;
    gap: 12px;
  }
  .company {
    position: absolute;
    left: 80px;
    top: 1960px;
    display: flex;
    align-items: center;
    gap: 24px;
  }
  .company-square { width: 64px; height: 64px; background: var(--royal); }
  .company-name {
    font-family: "Oswald", sans-serif;
    font-weight: 700;
    font-size: 84px;
    line-height: 1;
    color: var(--navy);
  }
  .cta {
    position: absolute;
    left: 373px;
    top: 2193px;
    width: 454px;
    height: 76px;
    background: var(--violet);
    color: #fff;
    font-weight: 700;
    font-size: 44px;
    display: flex;
    align-items: center;
    justify-content: center;
    box-shadow: 0 22px 18px -14px rgba(0,0,0,0.35);
  }
  .contact-icon { position: absolute; left: 540px; width: 124px; height: 124px; }
  .contact-icon.mail { top: 2384px; }
  .contact-icon.phone { top: 2618px; }
  .contact-line {
    position: absolute;
    left: 0;
    width: 1200px;
    text-align: center;
    color: var(--navy);
    font-weight: 700;
    font-size: 80px;
    line-height: 1;
  }
  .contact-line.email { top: 2510px; }
  .contact-line.phone-number { top: 2756px; }
  .web-bar {
    position: absolute;
    left: 225px;
    top: 2922px;
    width: 746px;
    height: 119px;
    background: var(--sky);
    color: #fff;
    font-size: 66px;
    font-weight: 500;
    display: flex;
    align-items: center;
    justify-content: center;
  }
</style>
</head>
<body>
<main class="flyer">
  <svg class="backdrop" viewBox="0 0 1200 2000" xmlns="http://www.w3.org/2000/svg">
    <defs>
      <linearGradient id="landscapeTone" x1="0" y1="0" x2="0" y2="1">
        <stop offset="0" stop-color="#6d78b4"/>
        <stop offset="0.5" stop-color="#4e5ea6"/>
        <stop offset="1" stop-color="#2f3f86"/>
      </linearGradient>
    </defs>
    <path role="img" aria-label="Photograph of a rocky canyon landscape at dusk in blue tones"
      fill="url(#landscapeTone)"
      d="M0,0 H1200 V1820 C900,1700 450,1460 0,1300 Z"/>
    <rect x="404" y="0" width="796" height="330" fill="#ffffff"/>
  </svg>

  <div class="brand-header">Plains Ledger</div>

  <div class="accent-bars"><span class="bar-dark"></span><span class="bar-light"></span></div>
  <p class="tagline"><strong>PlainsLedger</strong> is the premier source for<br>County Clerk Records and Mineral<br>Appraisal Data covering Texas, Oklahoma,<br>New Mexico and Colorado.</p>

  <div class="search">
    <div class="search-field">One Click, Every County</div>
    <div class="search-button">
      <svg width="30" height="30" viewBox="0 0 30 30" aria-hidden="true"><circle cx="17" cy="12" r="9" fill="none" stroke="#fff" stroke-width="3"/><line x1="10" y1="19" x2="3" y2="27" stroke="#fff" stroke-width="3.5" stroke-linecap="round"/></svg>
      Search
    </div>
  </div>

  <div class="company">
    <span class="company-square"></span>
    <span class="company-name">Plains Ledger</span>
  </div>

  <div class="cta">GET IN TOUCH</div>

  <svg class="contact-icon mail" viewBox="0 0 124 124" aria-hidden="true">
    <circle cx="62" cy="62" r="62" fill="var(--violet)"/>
    <rect x="30" y="40" width="64" height="44" rx="3" fill="none" stroke="#fff" stroke-width="5"/>
    <polyline points="30,42 62,66 94,42" fill="none" stroke="#fff" stroke-width="5"/>
  </svg>
  <div class="contact-line email">info@plainsledger.com</div>

  <svg class="contact-icon phone" viewBox="0 0 124 124" aria-hidden="true">
    <circle cx="62" cy="62" r="62" fill="var(--violet)"/>
    <path d="M28,50 C28,34 96,34 96,50 L96,58 L80,58 L78,48 C70,44 54,44 46,48 L44,58 L28,58 Z" fill="#fff"/>
    <path d="M44,60 L80,60 L90,88 L34,88 Z" fill="#fff"/>
    <circle cx="62" cy="74" r="8" fill="var(--violet)"/>
  </svg>
  <div class="contact-line phone-number">(214) 555-0182</div>

  <div class="web-bar">www.plainsledger.com</div>
</main>
</body>
</html>
```